Create a Magazine Ad for an asbestos law firm

we need an 8 X 13 ad to be on the back of a magazine cover. We have the text Attached and want a similar look and feel to our website : www.harborvale-claims.example. The ad should be targeted to white males 55 years or older who are conservative and worked in industry or industrial plants. The main offer is a free case review and trying to get them to call the telephone number.

Target Market(s)

White collar men who worked in industrial plants. Age 55 years or older.

Industry/Entity Type

Legal

Requirements
Must have
• Pictures of white middle class conservative man or man and woman
Nice to have
• look at www.harborvale-claims.example to an. idea of what we are looking for

```html
<!DOCTYPE html>
<html lang="en">
<head>
<meta charset="utf-8">
<title>Harborvale Claims – Mesothelioma Compensation</title>
<link href="https://fonts.googleapis.com/css2?family=Montserrat:wght@300;400;600;700&family=Roboto+Condensed:wght@400&display=swap" rel="stylesheet">
<style>
  :root{
    --bg:#4a7ff0;
    --bg-light:#5a95f2;
    --ink:#0e1640;
    --accent:#1c5be6;
    --accent-deep:#2d2cf5;
    --frame:#27327a;
    --white:#ffffff;
  }
  *{margin:0;padding:0;box-sizing:border-box}
  html,body{width:738px;height:1200px;overflow:hidden}
  body{background:var(--bg);font-family:"Montserrat",sans-serif;color:var(--ink)}
  .ad{position:relative;width:738px;height:1200px;overflow:hidden;background:linear-gradient(180deg,var(--bg) 0%,var(--bg) 70%,var(--bg-light) 100%)}
  .ad > *{position:absolute}
  .frame{left:17px;top:14px;width:698px;height:1137px;border:1px solid var(--frame)}
  .bg-word{right:-16px;top:40px;writing-mode:vertical-rl;transform:rotate(180deg);font-size:150px;font-weight:400;color:rgba(30,70,200,.16);letter-spacing:2px;line-height:1;white-space:nowrap}
  .photo{left:0;top:605px;width:420px;height:595px;background:radial-gradient(ellipse at 45% 55%,rgba(150,195,250,.75) 0%,rgba(110,160,245,.55) 45%,rgba(74,127,240,0) 75%)}
  .brand{left:403px;top:30px;display:flex;align-items:center;gap:8px}
  .brand-dot{width:30px;height:30px;border-radius:50%;background:var(--frame)}
  .brand-name{font-size:24px;font-weight:400;color:var(--frame);line-height:1}
  .brand-tag{left:463px;top:61px;font-family:"Roboto Condensed",sans-serif;font-size:9.5px;color:var(--frame)}
  .headline{left:50px;top:78px;line-height:1}
  .headline .light{font-size:31px;font-weight:300;display:block}
  .headline .strong{font-size:37px;font-weight:700;color:var(--accent);display:block}
  .headline .gap{margin-top:15px}
  .headline .strong.sm{font-size:30px}
  .trust{left:390px;top:124px;line-height:1}
  .trust .amount{font-size:44px;font-weight:700;color:var(--accent);display:block}
  .trust .light{font-size:23px;font-weight:300;display:block;margin-top:2px}
  .trust .strong{font-size:27px;font-weight:700;color:var(--accent);display:block;margin-top:8px}
  .body{font-size:11.6px;line-height:1.25;font-weight:400}
  .list{border-left:1px solid var(--ink);padding-left:5px;margin:4px 0 0 18px}
  .intro{left:28px;top:251px;width:330px}
  .help{left:26px;top:374px;width:330px}
  .tradesmen{left:370px;top:261px;width:335px}
  .how{left:369px;top:400px;font-size:22px;font-weight:300;line-height:1.27}
  .how b{font-weight:600;color:var(--accent-deep)}
  .how em{font-style:normal;color:var(--accent-deep)}
  .how-desc{left:369px;top:486px;width:330px}
  .eligible{left:24px;top:523px;font-size:15px;font-weight:700;line-height:1.2}
  .eligible-sub{left:27px;top:559px;width:320px;font-size:11.4px;font-weight:600;line-height:1.25}
  .cta-title{left:49px;top:633px;width:302px;text-align:center;font-size:15.5px;font-weight:700}
  .cta-bar{left:50px;top:657px;width:301px;height:26px;background:var(--accent-deep);border-radius:16px 0 0 0;color:var(--white);font-size:11.5px;font-weight:700;display:flex;align-items:center;justify-content:center}
  .cta-outline{left:55px;top:715px;width:296px;height:44px;border:1.5px solid var(--ink);border-radius:24px 0 0 0;color:var(--accent-deep);font-size:22px;font-weight:600;display:flex;align-items:center;justify-content:center}
  .settlements{left:380px;top:594px;border-left:1px solid var(--ink);padding-left:9px;width:320px;list-style:none}
  .settlements li{font-size:11.6px;line-height:1.25;margin-bottom:13.5px}
  .footer{left:0;top:1149px;width:738px;height:26px;background:var(--accent-deep);color:var(--white);font-size:11.5px;font-weight:700;display:flex;align-items:center;justify-content:center}
</style>
</head>
<body>
<div class="ad">
  <div class="bg-word" aria-hidden="true">Harborvale</div>
  <div class="photo" role="img" aria-label="Photo of an older couple embracing"></div>
  <div class="frame"></div>

  <div class="brand"><span class="brand-dot"></span><span class="brand-name">Harborvale Claims</span></div>
  <div class="brand-tag">Over 20 years of fighting for mesothelioma patients and families</div>

  <h1 class="headline">
    <span class="light">Diagnosed with</span>
    <span class="strong">Mesothelioma,</span>
    <span class="light gap">You could be Owed</span>
    <span class="strong sm">Compensation</span>
  </h1>

  <h2 class="trust">
    <span class="amount">$30 Billion</span>
    <span class="light">is Available in Trust for</span>
    <span class="strong">Mesothelioma Patients</span>
  </h2>

  <div class="body intro">
    <p>It's very likely you developed this disease through asbestos exposure. Mesothelioma patients are getting multi-million dollar settlements, decades later, fromt</p>
    <div class="list">Exposure to asbestos products,<br>Ex-employers, or<br>Talcum baby powder companies</div>
  </div>

  <div class="body help">
    <p>We can help you find out if you qualify for a<br>case in minutes</p>
    <div class="list" style="margin-top:12px">We'll analyze your situation at no cost,<br>Determine how much compensation you could be entitled too,<br>Show you the next steps to get what you're owed.</div>
  </div>

  <p class="body tradesmen">Tradesmen in many industries were negligently exposed to asbestos materials well into the 1990s. Whether you developed Mesothelioma yourself due to asbestos exposure or you're the surviving family of a lost loved one youcould be entitled to significant compensation</p>

  <h3 class="how">How much <b>Money</b> Can<br>People Receive from a<br><em>Mesothelioma</em> Case?</h3>

  <p class="body how-desc">Depending on where you were exposed and a few other factors, you can get a settlement from 6 to 7 figures. Here are a few examples of Mesothelioma Settlements received by our clients. These figures are the total compensation after all attorney fees and expenses are deducted.</p>

  <ul class="settlements">
    <li>$6,142,500<br>Exposed through heavy duty vehicles</li>
    <li>$6,033,510<br>Exposed through general contracting</li>
    <li>$5,939,010<br>Exposed through boat repair</li>
    <li>$3,921,750<br>Exposed through navy service</li>
    <li>$3,600,450<br>Exposed through navy service</li>
    <li style="margin-bottom:0">$2.5 Million<br>Exposed from Larkfield Talcum Baby Powder.</li>
  </ul>

  <p class="eligible">Find out if you're Eligible,<br>for FREE, in Minutes</p>
  <p class="eligible-sub">We'll evaluate your situation and tell you what your case could be worth</p>

  <p class="cta-title">Get your Free evaluation now!</p>
  <div class="cta-bar">CALL 1-XXX XXXX</div>
  <div class="cta-outline">Call now</div>

  <div class="footer">Calloway &amp; Brandt, LLP, Martin Calloway, Houston, TX</div>
</div>
</body>
</html>
```